Professionell und kommunikativ, kommen gerne wieder.
Zielgruppe
Wir transportieren Güter und Waren aller Art rund um die Welt. Hauptsächlich Luftfracht, aber auch per Schiff und an Land. Hauptsächlich richten wir uns damit an Firmenkunden, weniger an Privatkunden. Für unsere neue Website benötigen wir ein Design.
Aufgabenstellung
Wir benötigen ein Webdesign für den Relaunch unserer Website. Unsere Ideen für unsere neue Website haben wir bereits skizziert (Anlage). Diese Mockups bedürfen nun eines Designs.
Dazu ergänzend gelten die folgenden, formalen Vorgaben:
• 1140px breit, gerne auch Ideen für die Darstellung auf Smartphones und Tablets
• Logo links oben
• Navigation oben waagerecht
• Dropdown-Navigation am Desktop, Hamburger für die mobile Navigation
• Verwendung eines Grid-Systems wie Bootstrap
• Mindestschriftgröße für Mengentext: 16px (bei groß ausfallenden Fonts 15px)
Wir haben keine Hausschriftart und keine festgelegten Farben. Wir möchten aber unser Logo weiterverwenden und da bietet es sich natürlich an, auf dem Rot aufzubauen.

```html
<!DOCTYPE html>
<html lang="en">
<head>
<meta charset="utf-8">
<title>VELAFRACHT – Air Freight</title>
<link href="https://fonts.googleapis.com/css2?family=Hind:wght@400;500;600;700&display=swap" rel="stylesheet">
<style>
:root{
  --blue:#0b4a8c;
  --blue-dark:#0a3665;
  --red:#e31e24;
  --ink:#1c2a3a;
  --white:#ffffff;
  --line:#c9d0d8;
}
*{margin:0;padding:0;box-sizing:border-box}
html,body{width:978px;height:1200px;overflow:hidden}
body{position:relative;font-family:"Hind",Arial,sans-serif;color:var(--ink);background:var(--white)}
.abs{position:absolute}
a{color:inherit;text-decoration:none}

/* top bar */
.topbar{left:0;top:0;width:978px;height:23px;background:var(--blue);color:var(--white);font-size:8.5px}
.topbar .contact{left:183px;top:6px;display:flex;gap:8px;align-items:center}
.topbar .contact span{display:flex;align-items:center;gap:4px}
.topbar .quote{left:695px;top:6px}
.topbar .lang{left:762px;top:8px;display:flex;gap:7px;align-items:center}

/* header */
.header{left:0;top:23px;width:978px;height:42px;background:var(--white)}
.brand{left:183px;top:9px;display:flex;align-items:center;gap:5px;font-size:22px;font-weight:400;color:#555;letter-spacing:-0.5px}
.brand .dot{width:14px;height:14px;border-radius:50%;background:var(--red)}
.header .divider{left:336px;top:0;width:1px;height:42px;background:var(--blue)}
.nav{left:571px;top:10px;display:flex;align-items:center;font-size:8.5px;font-weight:500}
.nav a{padding:7px 10px 5px}
.nav .active{background:var(--red);color:var(--white);margin-right:4px}
.nav .caret{display:inline-block;margin-left:5px;border:3px solid transparent;border-top:3.5px solid var(--ink);vertical-align:1px}

/* hero */
.hero{left:0;top:65px;width:978px;height:379px;background:radial-gradient(ellipse at 50% 40%,#8a7a5e 0%,#4d4a43 40%,#2f3338 75%),#3a3a3a}
.hero::after{content:"";position:absolute;left:0;right:0;bottom:0;height:150px;background:linear-gradient(180deg,transparent,#5b4633)}
.hero-content{left:0;top:173px;width:978px;text-align:center;color:var(--white);z-index:2}
.hero-title{font-size:35px;font-weight:600;line-height:1}
.hero-text{width:400px;margin:14px auto 0;font-size:8.4px;line-height:15.5px}
.btn-red{display:inline-block;background:var(--red);color:var(--white);font-weight:600;font-size:8px;letter-spacing:.4px;padding:7px 10px 5px;margin-top:2px}
.pager{left:942px;top:245px;z-index:2;display:flex;flex-direction:column;align-items:center;gap:8px}
.pager i{display:block;width:3px;height:3px;border-radius:50%;background:var(--white)}
.pager i.on{width:6px;height:6px;background:var(--blue);border:1px solid var(--red)}

/* service tiles */
.tile{top:389px;width:107px;height:107px;color:var(--white);font-size:8.5px;z-index:3}
.tile span{position:absolute;left:10px;bottom:19px}
.tile.air{left:239px;width:112px;height:112px;top:387px;border:2px solid var(--red);background:linear-gradient(180deg,#7d7568,#4a4741 60%,#2f2e2c);font-weight:700;font-size:9.5px}
.tile.sea{left:374px;background:linear-gradient(180deg,#2b4466,#1f3d66 60%,#224569)}
.tile.land{left:506px;background:linear-gradient(135deg,#2d3f58,#5b2f36 50%,#203a5a)}
.tile.airline{left:639px;background:linear-gradient(135deg,#5a5d4c,#2a4670 45%,#1f4575)}

/* help */
.help-photo{left:183px;top:563px;width:201px;height:141px;background:linear-gradient(180deg,#b5b8b8 0%,#8a7c6a 45%,#6c5e50 100%)}
.help-vline{left:397px;top:563px;width:1px;height:141px;background:var(--line)}
.help-hline{left:397px;top:673px;width:397px;height:1px;background:var(--line)}
.help-title{left:423px;top:577px;font-size:27px;font-weight:700;color:var(--blue);line-height:1}
.help-title em{font-style:normal;color:var(--red)}
.help-text{left:423px;top:615px;width:360px;font-size:8px;line-height:12.3px}
.help-time{left:423px;top:651px;font-size:8px}
.help-actions{left:423px;top:678px;display:flex;font-size:8px;font-weight:600}
.help-actions div{display:flex;align-items:center;gap:8px;width:125px}
.icon-circle{width:20px;height:20px;border-radius:50%;background:var(--blue);display:flex;align-items:center;justify-content:center}

/* partners */
.partners{left:0;top:768px;width:978px;height:297px;background:var(--blue)}
.partners-title{left:0;top:837px;width:978px;text-align:center;font-size:25px;font-weight:700;color:var(--white);line-height:1}
.partners-title em{font-style:normal;color:var(--red)}
.partner{color:var(--white);font-size:15px;font-weight:700;letter-spacing:.5px;display:flex;align-items:center;gap:6px}
.partner i{display:block;width:12px;height:12px;background:var(--white)}

/* footer */
.footer{left:0;top:1065px;width:978px;height:135px;background:var(--blue-dark);color:var(--white)}
.footer-rule{left:183px;top:1064px;width:611px;height:2px;background:var(--red)}
.f-head{top:1086px;font-size:10px;font-weight:600;color:var(--red)}
.f-list{top:1109px;font-size:8px;line-height:12.3px;list-style:none}
.f-input{left:434px;width:170px;height:17px;background:var(--white);font-size:6px;color:#999;padding:6px 6px 0}
.f-send{left:434px;top:1147px;width:170px;height:19px;background:var(--red);font-size:8px;font-weight:600;text-align:center;padding-top:6px}
.f-brand{left:614px;top:1085px;display:flex;align-items:center;gap:5px;font-size:19px;color:var(--white);letter-spacing:-0.5px}
.f-brand .dot{width:12px;height:12px;border-radius:50%;background:var(--red)}
.f-copy{left:614px;top:1118px;font-size:8px}
.f-contact{left:614px;top:1140px;font-size:8px;line-height:12.3px}
.f-contact div{display:flex;align-items:center;gap:5px}
.totop{left:935px;top:1167px;width:18px;height:18px;border-radius:50%;background:var(--white);display:flex;align-items:center;justify-content:center}
</style>
</head>
<body>

<div class="abs topbar">
  <div class="abs contact">
    <span><svg width="7" height="7" viewBox="0 0 10 10"><path d="M2 0l2 2.5-1.2 1.2c.6 1.3 1.4 2.1 2.6 2.7L6.6 5.2 9.5 7 8.6 9.3C4 9.6.3 5.8.6 1.3z" fill="#fff"/></svg>+49 61230 45678</span>
    <span><svg width="7" height="6" viewBox="0 0 10 8"><rect width="10" height="8" fill="#fff"/><path d="M0 0l5 4 5-4" stroke="#0b4a8c" fill="none"/></svg>info@velafracht.com</span>
  </div>
  <div class="abs quote">Get a quote</div>
  <div class="abs lang">
    <svg width="9" height="6" viewBox="0 0 9 6"><rect width="9" height="6" fill="#fff"/><rect y="0" width="9" height="1" fill="#c33"/><rect y="2" width="9" height="1" fill="#c33"/><rect y="4" width="9" height="1" fill="#c33"/><rect width="4" height="3" fill="#2a4a8a"/></svg>
    <svg width="6" height="4" viewBox="0 0 6 4"><path d="M0 0h6L3 4z" fill="#fff"/></svg>
  </div>
</div>

<header class="abs header">
  <div class="abs brand">VELAFRACHT<i class="dot"></i></div>
  <div class="abs divider"></div>
  <nav class="abs nav">
    <a class="active" href="#">Home</a>
    <a href="#">Services<i class="caret"></i></a>
    <a href="#">About us</a>
    <a href="#">Contact</a>
  </nav>
</header>

<section class="abs hero" role="img" aria-label="Passenger jet facing the camera on an airport apron at sunset"></section>
<div class="abs hero-content">
  <h1 class="hero-title">Air Freight</h1>
  <p class="hero-text">The word cargo refers in particular to goods or produce being conveyed generally for commercial gain by ship, boat or aircraft, although the term is now often extended to cover all types of freight, including that carried by train, van, truck or container.</p>
  <a class="btn-red" href="#">READ MORE</a>
</div>
<div class="abs pager">
  <svg width="8" height="5" viewBox="0 0 8 5"><path d="M0 5l4-4 4 4" stroke="#fff" fill="none" stroke-width=".8"/></svg>
  <i class="on"></i><i></i><i></i><i></i>
  <svg width="8" height="5" viewBox="0 0 8 5"><path d="M0 0l4 4 4-4" stroke="#fff" fill="none" stroke-width=".8"/></svg>
</div>

<a class="abs tile air" href="#" role="img" aria-label="Jet on the apron at sunset"><span>Air Freight</span></a>
<a class="abs tile sea" href="#" role="img" aria-label="Container ship at port cranes"><span>Sea Freight</span></a>
<a class="abs tile land" href="#" role="img" aria-label="Red truck on the road"><span>Land Transport</span></a>
<a class="abs tile airline" href="#" role="img" aria-label="Close-up of an aircraft tail"><span>Airline Services</span></a>

<div class="abs help-photo" role="img" aria-label="Cargo pallet under net beside an aircraft on the apron"></div>
<div class="abs help-vline"></div>
<div class="abs help-hline"></div>
<h2 class="abs help-title">Need <em>help</em>?</h2>
<p class="abs help-text">On weekday your message will usually answered within 24 hours. We’re open Monday trough Friday excluding national and regional holidays. Ofice hours from 8 am until 4.30 pm</p>
<p class="abs help-time">It is 12:42 pm in Gießen right now</p>
<div class="abs help-actions">
  <div><span class="icon-circle"><svg width="10" height="10" viewBox="0 0 10 10"><path d="M2 0l2 2.5-1.2 1.2c.6 1.3 1.4 2.1 2.6 2.7L6.6 5.2 9.5 7 8.6 9.3C4 9.6.3 5.8.6 1.3z" fill="#e31e24"/></svg></span>+49 61230 45678</div>
  <div><span class="icon-circle"><svg width="9" height="9" viewBox="0 0 10 10"><rect x="0" y="2" width="10" height="8" fill="#e31e24"/><rect x="2" y="0" width="1.5" height="3" fill="#e31e24"/><rect x="6.5" y="0" width="1.5" height="3" fill="#e31e24"/><path d="M2 5h6M2 7.5h6" stroke="#0b4a8c"/></svg></span>Make a date</div>
  <div><span class="icon-circle"><svg width="11" height="9" viewBox="0 0 12 10"><path d="M0 4l2 0 2 1.5L10 2c1-.5 2 0 1.5 1L5 7H1z" fill="#e31e24"/><rect x="0" y="8.5" width="12" height="1.3" fill="#e31e24"/></svg></span>Get a quote</div>
</div>

<section class="abs partners" role="img" aria-label="Faint dotted world map background"></section>
<h2 class="abs partners-title">Our <em>Partners</em> and <em>Clients</em></h2>
<div class="abs partner" style="left:292px;top:903px">CEDRA AIR</div>
<div class="abs partner" style="left:580px;top:903px"><i></i>LUSAVIA</div>
<div class="abs partner" style="left:290px;top:958px">CARIBWING</div>
<div class="abs partner" style="left:580px;top:958px">ALINEA NETWORK</div>

<footer class="abs footer"></footer>
<div class="abs footer-rule"></div>
<h3 class="abs f-head" style="left:194px">Links</h3>
<h3 class="abs f-head" style="left:314px">Legal</h3>
<h3 class="abs f-head" style="left:434px">Callback service</h3>
<ul class="abs f-list" style="left:194px;color:#fff"><li>&gt;&gt; Home</li><li>&gt;&gt; Services</li><li>&gt;&gt; About us</li><li>&gt;&gt; Contact</li></ul>
<ul class="abs f-list" style="left:314px;color:#fff"><li>&gt;&gt; imprint</li><li>&gt;&gt; Data Protection</li></ul>
<div class="abs f-input" style="top:1108px">Name</div>
<div class="abs f-input" style="top:1127px">Phone</div>
<div class="abs f-send" style="color:#fff">Send</div>
<div class="abs f-brand">VELAFRACHT<i class="dot"></i></div>
<p class="abs f-copy" style="color:#fff">© 2023 VELAFRACHT. All rights reserved.</p>
<div class="abs f-contact" style="color:#fff">
  <div><svg width="7" height="7" viewBox="0 0 10 10"><path d="M2 0l2 2.5-1.2 1.2c.6 1.3 1.4 2.1 2.6 2.7L6.6 5.2 9.5 7 8.6 9.3C4 9.6.3 5.8.6 1.3z" fill="#fff"/></svg>+49 61230 45678</div>
  <div><svg width="7" height="6" viewBox="0 0 10 8"><rect width="10" height="8" fill="#fff"/><path d="M0 0l5 4 5-4" stroke="#0a3665" fill="none"/></svg>info@velafracht.com</div>
</div>
<a class="abs totop" href="#"><svg width="6" height="7" viewBox="0 0 6 8"><path d="M3 8V1M0 3.5L3 .5 6 3.5" stroke="#0a3665" fill="none" stroke-width=".8"/></svg></a>

</body>
</html>
```